Wexbridge Home Services Web Site

Design Web site with 3-4 pages: Home, About Us, Services and Order form / Schedule Appointment (which will likely be link to Tallyo App and Ledgerpine integration.)
Services include: Dryer Vent Cleaning, AC Cleaning, Difficult-to-Reach Light Bulb replacement, Wood Repair and Home Maintenance Plans including Fire Safety Checks and Filter Replacement.

Target Market(s)

Luxury Home Owners, Professionals (Dr's/lawyers) and Seniors

Industry/Entity Type

Home Maintenance

Coding

Coded - Design and coding required

Requirements
Must have
• Tagline - Where Home Maintenance is Effortless

```html
<!DOCTYPE html>
<html lang="en">
<head>
<meta charset="utf-8">
<title>Wexbridge Home Services</title>
<link href="https://fonts.googleapis.com/css2?family=Roboto:wght@400;500;700;900&family=Lato:wght@400;700&display=swap" rel="stylesheet">
<style>
:root{
  --gold:#e0aa2a;
  --gray:#6b6b6b;
  --dark:#333;
  --cream:#fbf4e8;
  --footer:#202020;
  --white:#fff;
}
*{margin:0;padding:0;box-sizing:border-box}
html,body{width:1200px;height:3550px;overflow:hidden}
body{font-family:"Roboto",sans-serif;color:var(--dark);background:#fff;position:relative}
.abs{position:absolute}
.btn{position:absolute;display:flex;align-items:center;justify-content:center;background:var(--gold);color:#fff;font-weight:700;font-size:17px;border-radius:4px;text-transform:uppercase}
.btn-outline{background:transparent;border:2px solid #fff;border-radius:3px}
.photo{position:absolute}
.rule{position:absolute;height:3px;background:var(--gold);border-radius:2px}

/* header */
.site-header{position:absolute;left:0;top:0;width:1200px;height:135px}
.brand{position:absolute;left:112px;top:18px;width:170px;text-align:center}
.brand-mark{width:34px;height:34px;border-radius:50%;background:var(--gold);margin:0 auto 8px}
.brand-name{font-weight:700;color:var(--gold);font-size:24px;letter-spacing:3px;line-height:28px}
.brand-sub{font-size:11px;color:var(--gray);letter-spacing:1px}
.info{position:absolute;top:14px;display:flex;gap:14px;align-items:center}
.info-icon{width:50px;height:50px;border-radius:50%;background:#6e6e6e;display:flex;align-items:center;justify-content:center}
.info b{display:block;font-size:16px;font-weight:500;color:#222}
.info span{font-size:15px;color:#444}
.nav{position:absolute;left:345px;top:80px;width:855px;height:55px;background:var(--gold);border-radius:30px 0 0 0;display:flex;align-items:center;padding-left:35px;gap:42px}
.nav a{color:#fff;font-weight:700;font-size:17px;text-decoration:none}
.nav a.active{color:#7a6a55}

/* hero */
.hero{position:absolute;left:0;top:135px;width:1200px;height:530px;background:linear-gradient(90deg,#f3f0ec 0%,#ece5dc 35%,#c9b8a3 65%,#a89684 100%)}
.hero h1{position:absolute;left:120px;top:115px;font-size:54px;line-height:64px;font-weight:700;color:#6e6e6e}
.hero h1 em{font-style:normal;color:var(--gold);font-weight:900}
.hero p{position:absolute;left:120px;top:250px;width:450px;font-family:"Lato",sans-serif;font-size:16px;line-height:30px;color:#555}
.arrow{position:absolute;top:240px;width:50px;height:50px;border-radius:50%;background:var(--gold);display:flex;align-items:center;justify-content:center}

/* schedule band */
.band{position:absolute;left:0;top:665px;width:1200px;height:166px;background:var(--gold)}
.band h2{text-align:center;color:#fff;font-size:27px;font-weight:700;margin-top:25px}
.field{position:absolute;top:75px;width:187px;height:57px;background:#fff;font-size:15px;color:#777;padding-left:13px;display:flex;align-items:center}

/* section title */
.title{font-size:44px;font-weight:500;color:#6b6b6b}
.title b{color:var(--gold);font-weight:900}

/* services */
.services{position:absolute;left:0;top:1520px;width:1200px;height:625px;background:var(--cream)}
.card{position:absolute;top:222px;width:230px;height:316px;background:#fff;border-radius:115px 115px 6px 6px;overflow:hidden}
.card .photo{left:0;top:0;width:230px;height:263px}
.card .label{position:absolute;left:0;bottom:0;width:100%;height:53px;display:flex;align-items:center;justify-content:center;font-weight:500;font-size:17px;color:#666}
.card.on .label{background:var(--gold);color:#fff}

/* why */
.why-list{position:absolute;left:112px;top:2412px;list-style:none}
.why-list li{display:flex;align-items:center;gap:22px;height:56px;font-size:22px;color:#222}

/* cta */
.cta{position:absolute;left:0;top:2780px;width:1200px;height:345px;background:linear-gradient(180deg,#8e8e93,#7c7c80)}
.cta h2{position:absolute;left:0;top:80px;width:1200px;text-align:center;color:#fff;font-size:40px;line-height:56px;font-weight:700}

/* footer */
.footer{position:absolute;left:0;top:3125px;width:1200px;height:425px;background:var(--footer);color:#fff}
.footer h4{font-size:21px;font-weight:700;margin-bottom:16px}
.links{list-style:none}
.links li{display:flex;gap:12px;align-items:center;font-size:15px;height:30px}
.contact li{display:flex;gap:20px;font-size:15px;margin-bottom:26px;line-height:21px;list-style:none}
.tagline{font-size:15px;color:#fff;margin-top:12px;letter-spacing:.5px}
</style>
</head>
<body>

<header class="site-header">
  <div class="brand">
    <div class="brand-mark"></div>
    <div class="brand-name">WEXBRIDGE</div>
    <div class="brand-sub">HOME SERVICES</div>
  </div>
  <div class="info" style="left:383px">
    <div class="info-icon"><svg width="18" height="22" viewBox="0 0 18 22"><path d="M9 0a8 8 0 0 0-8 8c0 6 8 14 8 14s8-8 8-14a8 8 0 0 0-8-8z" fill="#e0aa2a"/></svg></div>
    <div><b>Address</b><span>Lorem ipsum dolor sit amet, 2355</span></div>
  </div>
  <div class="info" style="left:794px">
    <div class="info-icon"><svg width="22" height="16" viewBox="0 0 22 16"><rect width="22" height="16" rx="2" fill="#e0aa2a"/><path d="M1 2l10 7 10-7" stroke="#6e6e6e" stroke-width="1.5" fill="none"/></svg></div>
    <div><b>Email Us</b><span>info@wexbridgehomeservices.com</span></div>
  </div>
  <nav class="nav">
    <a class="active">HOME</a><a>ABOUT US</a><a>SERVICES</a><a>CONTACT US</a><a>SCHEDULE APPOINTMENT</a>
  </nav>
</header>

<section class="hero" role="img" aria-label="Mother and child doing laundry in a bright kitchen">
  <div class="abs" style="left:0;top:0;width:700px;height:530px;background:linear-gradient(90deg,rgba(255,255,255,.85),rgba(255,255,255,0))"></div>
  <div class="arrow" style="left:45px"><svg width="14" height="20"><path d="M11 2L3 10l8 8" stroke="#222" stroke-width="2" fill="none"/></svg></div>
  <div class="arrow" style="left:1107px"><svg width="14" height="20"><path d="M3 2l8 8-8 8" stroke="#222" stroke-width="2" fill="none"/></svg></div>
  <h1>YOUR HOME.<br><em>OUR EXPERTISE</em></h1>
  <p>Reliable home maintenance solutions – from vents and filters to wood repair and fire safety checks.</p>
  <div class="btn" style="left:120px;top:335px;width:270px;height:56px">Schedule Appointment</div>
</section>

<section class="band">
  <h2>SCHEDULE SERVICE NOW</h2>
  <div class="field" style="left:112px">Name</div>
  <div class="field" style="left:309px">Email</div>
  <div class="field" style="left:507px">Phone</div>
  <div class="field" style="left:704px;justify-content:space-between;padding-right:12px">Select Service<svg width="12" height="8"><path d="M1 1l5 5 5-5" stroke="#555" stroke-width="1.5" fill="none"/></svg></div>
  <div class="btn btn-outline" style="left:902px;top:75px;width:187px;height:57px;font-size:15px">Schedule Services</div>
</section>

<section class="about">
  <svg class="abs" style="left:112px;top:928px" width="405" height="490"><path d="M1 487V230 C1 120 60 40 150 20" stroke="#e0aa2a" stroke-width="2" fill="none"/><path d="M1 487H403V470" stroke="#e0aa2a" stroke-width="2" fill="none"/></svg>
  <div class="photo" style="left:138px;top:928px;width:403px;height:471px;border-radius:202px 202px 0 0;background:linear-gradient(160deg,#5f6b78,#2f3a4a 60%,#c9a640)" role="img" aria-label="Technician wiping an oven door with yellow gloves"></div>
  <h2 class="title abs" style="left:641px;top:975px">
    <b>WHO</b> WE ARE <span style="display:inline-block;width:48px;height:2px;background:var(--gold);vertical-align:middle;margin-left:10px"></span>
  </h2>
  <div class="rule" style="left:641px;top:1066px;width:60px"></div>
  <p class="abs" style="left:641px;top:1115px;width:440px;font-family:Lato,sans-serif;font-size:16px;line-height:26px;color:#555">At Wexbridge Homes, we believe every household deserves proactive care, not just emergency fixes. Our mission is to keep your home safe, functional, and comfortable year-round. From cleaning vents to ensuring fire safety, we focus on the details that matter most.</p>
  <div class="btn" style="left:641px;top:1274px;width:138px;height:56px">Read More</div>
</section>

<section class="services">
  <h2 class="title" style="text-align:center;margin-top:42px"><b>OUR</b> SERVICES</h2>
  <svg class="abs" style="left:405px;top:105px" width="420" height="30"><path d="M0 16H42M378 16H420" stroke="#e0aa2a" stroke-width="2"/></svg>
  <div class="rule" style="left:570px;top:119px;width:60px"></div>
  <p style="text-align:center;font-size:16px;color:#555;margin-top:46px">We offer a wide range of services to cover all your essential home needs.</p>
  <div class="card" style="left:112px"><div class="photo" style="background:linear-gradient(160deg,#eef1f1,#c8d3d2)" role="img" aria-label="Woman cleaning an air unit vent"></div><div class="label">Dryer Vent Cleaning</div></div>
  <div class="card on" style="left:360px"><div class="photo" style="background:linear-gradient(160deg,#f2f2f2,#bdbdbd)" role="img" aria-label="Hands changing a light bulb"></div><div class="label">Light Bulb Replacement</div></div>
  <div class="card" style="left:609px"><div class="photo" style="background:linear-gradient(160deg,#c99452,#e7c58f)" role="img" aria-label="Hands repairing a wooden window frame"></div><div class="label">Wood Repair</div></div>
  <div class="card" style="left:858px"><div class="photo" style="background:linear-gradient(160deg,#d8d4cc,#3c4258)" role="img" aria-label="Technician inspecting pipes under a sink"></div><div class="label">Maintenance Plans</div></div>
</section>

<section class="why">
  <h2 class="title abs" style="left:112px;top:2245px;line-height:54px"><b>WHY CHOOSE</b><br>WEXBRIDGE HOMES</h2>
  <div class="rule" style="left:112px;top:2378px;width:60px"></div>
  <ul class="why-list">
    <li><svg width="32" height="32"><circle cx="16" cy="16" r="13" stroke="#e0aa2a" stroke-width="2" fill="none"/><path d="M10 16l4 4 8-8" stroke="#e0aa2a" stroke-width="2" fill="none"/></svg>Trusted &amp; Reliable</li>
    <li><svg width="32" height="32"><circle cx="16" cy="14" r="9" stroke="#e0aa2a" stroke-width="2" fill="none"/><path d="M10 22l-3 8 9-4 9 4-3-8" stroke="#e0aa2a" stroke-width="2" fill="none"/></svg>Professional Quality</li>
    <li><svg width="32" height="32"><path d="M16 3l11 4v8c0 8-6 13-11 14C11 28 5 23 5 15V7z" stroke="#e0aa2a" stroke-width="2" fill="none"/><path d="M11 16l4 4 7-7" stroke="#e0aa2a" stroke-width="2" fill="none"/></svg>Safety-Focused</li>
    <li><svg width="32" height="32"><circle cx="16" cy="17" r="12" stroke="#e0aa2a" stroke-width="2" fill="none"/><path d="M16 10v7l5 3" stroke="#e0aa2a" stroke-width="2" fill="none"/></svg>Convenient Scheduling</li>
  </ul>
  <svg class="abs" style="left:708px;top:2240px" width="376" height="458"><path d="M2 456V446M2 456H374V190C374 90 300 15 200 2" stroke="#6b6b6b" stroke-width="2" fill="none"/></svg>
  <div class="photo" style="left:652px;top:2222px;width:375px;height:448px;border-radius:188px 188px 0 0;background:linear-gradient(160deg,#e8e2d6,#8a6a4e 55%,#d9cfc2)" role="img" aria-label="Father and child loading a washing machine"></div>
</section>

<section class="cta" role="img" aria-label="Person vacuuming a living room floor">
  <h2>KEEP YOUR HOME SAFE, CLEAN, AND RUNNING<br>SMOOTHLY – BOOK TODAY!</h2>
  <div class="abs" style="left:278px;top:220px;display:flex;align-items:center;gap:12px;color:#fff;font-size:31px;font-weight:500">
    <svg width="32" height="32" viewBox="0 0 24 24"><path d="M6.6 10.8a15 15 0 0 0 6.6 6.6l2.2-2.2c.3-.3.7-.4 1-.2 1.1.4 2.3.6 3.6.6.6 0 1 .4 1 1V20c0 .6-.4 1-1 1A17 17 0 0 1 3 4c0-.6.4-1 1-1h3.5c.6 0 1 .4 1 1 0 1.3.2 2.5.6 3.6.1.3 0 .7-.2 1z" fill="#fff"/></svg>
    + 1 888-888-8888
  </div>
  <div class="btn btn-outline" style="left:620px;top:212px;width:275px;height:55px">Book Now</div>
</section>

<footer class="footer">
  <div class="abs" style="left:112px;top:90px;width:305px;text-align:center">
    <div style="width:70px;height:70px;border-radius:50%;background:var(--gold);margin:0 auto 18px"></div>
    <div style="color:var(--gold);font-weight:700;font-size:46px;letter-spacing:5px;line-height:52px">WEXBRIDGE</div>
    <div style="color:var(--gold);font-size:22px;letter-spacing:1px">HOME SERVICES</div>
    <div class="tagline">Where Home Maintenance is Effortless</div>
  </div>
  <div class="abs" style="left:546px;top:100px">
    <h4>QUICK LINKS</h4>
    <ul class="links">
      <li><svg width="14" height="12"><path d="M1 1l5 5-5 5M7 1l5 5-5 5" stroke="#e0aa2a" stroke-width="1.6" fill="none"/></svg>Home</li>
      <li><svg width="14" height="12"><path d="M1 1l5 5-5 5M7 1l5 5-5 5" stroke="#e0aa2a" stroke-width="1.6" fill="none"/></svg>About Us</li>
      <li><svg width="14" height="12"><path d="M1 1l5 5-5 5M7 1l5 5-5 5" stroke="#e0aa2a" stroke-width="1.6" fill="none"/></svg>Services</li>
      <li><svg width="14" height="12"><path d="M1 1l5 5-5 5M7 1l5 5-5 5" stroke="#e0aa2a" stroke-width="1.6" fill="none"/></svg>Contact Us</li>
      <li><svg width="14" height="12"><path d="M1 1l5 5-5 5M7 1l5 5-5 5" stroke="#e0aa2a" stroke-width="1.6" fill="none"/></svg>Schedule Appointment</li>
    </ul>
  </div>
  <div class="abs" style="left:816px;top:100px;width:290px">
    <h4>CONTACT INFO</h4>
    <ul class="contact">
      <li><svg width="14" height="18" viewBox="0 0 18 22"><path d="M9 0a8 8 0 0 0-8 8c0 6 8 14 8 14s8-8 8-14a8 8 0 0 0-8-8z" fill="#e0aa2a"/></svg><span>2545 enim ipsam voluptatem quia 2458</span></li>
      <li><svg width="16" height="16" viewBox="0 0 24 24"><path d="M6.6 10.8a15 15 0 0 0 6.6 6.6l2.2-2.2c.3-.3.7-.4 1-.2 1.1.4 2.3.6 3.6.6.6 0 1 .4 1 1V20c0 .6-.4 1-1 1A17 17 0 0 1 3 4c0-.6.4-1 1-1h3.5c.6 0 1 .4 1 1 0 1.3.2 2.5.6 3.6.1.3 0 .7-.2 1z" fill="#e0aa2a"/></svg><span>+1 (888)-888-8888</span></li>
      <li><svg width="16" height="12"><rect width="16" height="12" rx="1" fill="#e0aa2a"/><path d="M1 1l7 5 7-5" stroke="#202020" fill="none"/></svg><span>info@wexbridgehomes.com</span></li>
    </ul>
  </div>
  <p class="abs" style="left:0;top:380px;width:1200px;text-align:center;font-size:15px">Copyright 2025. Wexbridge Homes. All Rights Reserved</p>
</footer>

</body>
</html>
```